I need podcast cover art that could also be incorporated into a website and social media accounts. I originally planned on calling the podcast "Clinical Outreach Hub" but need to change it to "Clinical Outreach Circle," and its purpose is to educate and inspire people on how we can deliver more affordable, higher quality health care in the United States. The target audience is anyone working in a healthcare related industry (doctors, nurses, healthcare insurers, policymakers involved in writing healthcare policy, etc...). The program will be well-researched and the tone will be upbeat. I will be interviewing experts in healthcare delivery including innovators who have come up with creative solutions to improving healthcare quality where they work. I want to keep the design very clean, simple, and modern looking. Thank you so much - I am looking forward to seeing your designs!

Target Market(s)

working professionals and students in healthcare-related fields

Industry/Entity Type

Health Care

Font styles to use
Sans Serif

Colors

Designer to choose colors to be used in the design.

Requirements
Must have
• very clean, simple and modern looking

```html
<!DOCTYPE html>
<html lang="en">
<head>
<meta charset="utf-8">
<title>Clinical Outreach Circle — Podcast Cover</title>
<link rel="stylesheet" href="https://fonts.googleapis.com/css2?family=Archivo+Black&family=Roboto+Condensed:wght@700&display=swap">
<style>
  :root {
    --teal-dark: #2d5560;
    --teal-mid: #8fb3bb;
    --mist: #c8dfe4;
    --mist-light: #d5e8ec;
    --ring: #ffffff;
    --title: #ffffff;
  }
  html, body {
    margin: 0;
    padding: 0;
    width: 1200px;
    height: 1200px;
    overflow: hidden;
    background: #ffffff;
  }
  .cover {
    position: relative;
    width: 1200px;
    height: 1200px;
    overflow: hidden;
  }
  .cover__backdrop {
    position: absolute;
    inset: 0;
    background:
      radial-gradient(circle at 15% 55%, #7fa4ad 0%, rgba(127,164,173,0) 35%),
      radial-gradient(circle at 90% 8%, #5f858f 0%, rgba(95,133,143,0) 30%),
      linear-gradient(135deg, #c6dde2 0%, #e4eef0 45%, #a9c4ca 100%);
  }
  .cover__art {
    position: absolute;
    inset: 0;
    width: 1200px;
    height: 1200px;
  }
  .tagline {
    font-family: "Roboto Condensed", "Arial Narrow", sans-serif;
    font-weight: 700;
    font-size: 53px;
    fill: var(--teal-dark);
    letter-spacing: -0.5px;
  }
  .show-title {
    font-family: "Archivo Black", "Arial Black", sans-serif;
    font-size: 122px;
    fill: var(--title);
    letter-spacing: -2px;
  }
</style>
</head>
<body>
  <main class="cover">
    <div class="cover__backdrop" role="img" aria-label="Soft-focus photograph of glass molecular model spheres joined by rods, in cool teal tones"></div>

    <svg class="cover__art" viewBox="0 0 1200 1200" xmlns="http://www.w3.org/2000/svg">
      <defs>
        <clipPath id="badge-clip">
          <circle cx="896" cy="771" r="654"/>
        </clipPath>
      </defs>

      <!-- badge disc with ring -->
      <circle class="badge-ring" cx="896" cy="771" r="662" fill="var(--ring)"/>
      <circle class="badge-disc" cx="896" cy="771" r="654" fill="var(--mist)"/>

      <g clip-path="url(#badge-clip)">
        <!-- long shadow of cross -->
        <polygon class="cross-shadow" points="710,296 933,296 1200,640 1200,1000 710,376" fill="var(--mist-light)"/>
        <polygon class="cross-shadow" points="788,217 856,217 1200,660 1200,760" fill="var(--mist-light)" opacity="0.6"/>
        <!-- long shadow of title -->
        <polygon class="title-shadow" points="320,668 1097,668 1200,768 1200,1200 860,1200 320,720" fill="var(--teal-dark)"/>
      </g>

      <!-- medical cross -->
      <g class="medical-cross" fill="var(--teal-dark)">
        <rect x="788" y="217" width="68" height="223"/>
        <rect x="710" y="296" width="223" height="66"/>
      </g>

      <!-- tagline -->
      <text class="tagline" x="1084" y="566" text-anchor="end">Interviewing Experts in</text>
      <text class="tagline" x="1084" y="643" text-anchor="end">Healthcare Delivery</text>

      <!-- show title -->
      <text class="show-title" x="1093" y="763" text-anchor="end">CLINICAL</text>
      <text class="show-title" x="1093" y="890" text-anchor="end">OUTREACH</text>
      <text class="show-title" x="1093" y="1024" text-anchor="end">CIRCLE</text>
    </svg>
  </main>
</body>
</html>
```